Lake of the Ozarks Anniversary Flag

Looking for a flag design that incorporates the outline of the Lake of the Ozarks on a white background with some additional wording/ design incorporated. Would like the lake outline in Navy Blue. On the top of the flag "LAKE OF THE OZARKS" in all caps (possibly also in Navy Blue with a bright red outline. In the background, large and centered in subdued gray "90th." Bottom left corner "1931" and bottom right corner "2021." Possibly also add a compass somewhere (possibly in the void to the middle left area. This is a flag being designed for boats that is to commemorate the 90th anniversary of Lake of the Ozarks this year. I have a couple more lake outlines I have screenshotted but this website won't seem to download them. I can send them separate if that assists.

```html
<!DOCTYPE html>
<html lang="en">
<head>
<meta charset="utf-8">
<title>Lake of the Ozarks 90th Anniversary Flag</title>
<link rel="stylesheet" href="https://fonts.googleapis.com/css2?family=Graduate&display=swap">
<style>
  :root {
    --flag-white: #ffffff;
    --navy: #24338f;
    --bright-red: #e8212e;
    --subdued-gray: #d3d3d4;
    --page-bg: #ffffff;
  }
  html, body {
    margin: 0;
    padding: 0;
    width: 1200px;
    height: 716px;
    overflow: hidden;
    background: var(--page-bg);
  }
  .flag {
    display: block;
    width: 1200px;
    height: 716px;
  }
  .flag__field { fill: var(--flag-white); }
  .stripe--navy { fill: var(--navy); }
  .stripe--red { fill: var(--bright-red); }
  .headline {
    font-family: "Graduate", "Georgia", serif;
    fill: var(--navy);
  }
  .title { font-size: 96px; }
  .year { font-size: 94px; }
  .anniversary {
    font-family: "Graduate", "Georgia", serif;
    fill: var(--subdued-gray);
  }
  .anniversary__number { font-size: 430px; }
  .anniversary__suffix { font-size: 210px; }
  .compass__ring { fill: none; stroke: var(--navy); stroke-width: 2; }
  .compass__point { fill: var(--navy); }
  .compass__point--light { fill: var(--flag-white); stroke: var(--navy); stroke-width: 1.5; }
  .compass__label {
    font-family: "Graduate", "Georgia", serif;
    font-size: 13px;
    fill: var(--navy);
    text-anchor: middle;
  }
</style>
</head>
<body>
<svg class="flag" viewBox="0 0 1200 716" xmlns="http://www.w3.org/2000/svg" aria-label="Lake of the Ozarks 90th anniversary flag">
  <defs>
    <radialGradient id="lake-tone" cx="50%" cy="50%" r="50%">
      <stop offset="0%" stop-color="#24338f" stop-opacity="0.5"/>
      <stop offset="70%" stop-color="#24338f" stop-opacity="0.2"/>
      <stop offset="100%" stop-color="#24338f" stop-opacity="0"/>
    </radialGradient>
  </defs>

  <rect class="flag__field" x="0" y="0" width="1200" height="716"/>

  <rect class="stripe--navy" x="0" y="0" width="1200" height="14"/>
  <rect class="stripe--red" x="0" y="24" width="1200" height="7"/>
  <rect class="stripe--red" x="0" y="686" width="1200" height="7"/>
  <rect class="stripe--navy" x="0" y="701" width="1200" height="15"/>

  <g class="anniversary">
    <text class="anniversary__number" x="49" y="524" textLength="780" lengthAdjust="spacingAndGlyphs">90</text>
    <text class="anniversary__suffix" x="822" y="384" textLength="325" lengthAdjust="spacingAndGlyphs">th</text>
  </g>

  <ellipse role="img" aria-label="Navy outline map of the Lake of the Ozarks"
           cx="548" cy="414" rx="362" ry="255" fill="url(#lake-tone)"/>

  <text class="headline title" x="53" y="132" textLength="1094" lengthAdjust="spacingAndGlyphs">LAKE OF THE OZARKS</text>

  <text class="headline year" x="49" y="660" textLength="216" lengthAdjust="spacingAndGlyphs">1931</text>
  <text class="headline year" x="919" y="660" textLength="226" lengthAdjust="spacingAndGlyphs">2021</text>

  <g class="compass" transform="translate(1038 482)">
    <circle class="compass__ring" r="36"/>
    <circle class="compass__ring" r="28"/>
    <polygon class="compass__point" points="0,-48 6,0 0,0"/>
    <polygon class="compass__point--light" points="0,-48 -6,0 0,0"/>
    <polygon class="compass__point" points="0,48 -6,0 0,0"/>
    <polygon class="compass__point--light" points="0,48 6,0 0,0"/>
    <polygon class="compass__point" points="48,0 0,6 0,0"/>
    <polygon class="compass__point--light" points="48,0 0,-6 0,0"/>
    <polygon class="compass__point" points="-48,0 0,-6 0,0"/>
    <polygon class="compass__point--light" points="-48,0 0,6 0,0"/>
    <text class="compass__label" x="0" y="-54">N</text>
    <text class="compass__label" x="0" y="66">S</text>
    <text class="compass__label" x="60" y="5">E</text>
    <text class="compass__label" x="-62" y="5">W</text>
  </g>
</svg>
</body>
</html>
```